Puslishing House Needs poster Design for Medical Book

We need an advertisement desing for a medical book on cardiology named "Vertentes" (Hypertension), which 2nd Edition we launched last August. What makes this book special is that this is the first time in history that a hypertension book has a second edition in Brazil and was written by the Vascular Unit of the Southern Clinical Guild of Heart Studies in comemoration in its 100 years. The two news about this book is that we sold 1000 units since we launched (which is good) and we have now an ebook version for all tablet, smartphones and readers. From this month on it is going to happen importants hypertension meetings and we want to promote this two news about this book - 1000 units sold and ebook version. We would like to see designs that use orange (the publishing house color) and communicate celebration.

Target Market(s)

Doctors Specialist from several segments like Cardiology, Endocrinology, Nephrology, Nutrition. Most of the target are man with 50 years-old.

Industry/Entity Type

Medical

Requirements
Must have
• The adverstisement must have the attached book cover and publishing house logo (Marlowan) using only the name (without the tree) or the complete logo.
Should not have
• The design should not use old-style, serif fonts like Times new Roman.

```html
<!DOCTYPE html>
<html lang="en">
<head>
<meta charset="utf-8">
<title>Vertentes 2ª Edição – Poster</title>
<link href="https://fonts.googleapis.com/css2?family=Oswald:wght@300;400;700&display=swap" rel="stylesheet">
<style>
  :root{
    --backdrop:#d9d4cc;
    --cream:#f2f0e4;
    --orange:#f07f1e;
    --orange-deep:#e8761a;
    --green:#1f6a3a;
    --green-dark:#1d4f2e;
    --ink:#111111;
    --white:#ffffff;
    --badge-blue:#1b4f9c;
  }
  *{margin:0;padding:0;box-sizing:border-box}
  html,body{width:861px;height:1200px;overflow:hidden;background:var(--backdrop)}
  .canvas{position:relative;width:861px;height:1200px}
  .poster{position:absolute;left:32px;top:39px;width:799px;height:1129px;background:var(--cream);overflow:hidden}
  .poster-shapes{position:absolute;inset:0}
  .title{position:absolute;left:110px;top:70px;width:640px;text-align:center;font-family:'Oswald',sans-serif;font-weight:700;font-size:122px;line-height:1;color:var(--orange);letter-spacing:1px}
  .edition{position:absolute;right:84px;top:170px;font-family:'Oswald',sans-serif;font-weight:300;font-size:34px;color:var(--green-dark)}
  .book-stack{position:absolute;left:37px;top:202px;width:455px;height:535px}
  .badge{position:absolute;left:515px;top:684px;width:258px;height:190px}
  .badge-label{position:absolute;left:565px;top:748px;width:165px;text-align:center;font-family:'Oswald',sans-serif;color:var(--white);line-height:1}
  .badge-number{font-size:44px;font-weight:400;display:block}
  .badge-units{font-size:24px;font-weight:300;display:block}
  .publisher{position:absolute;left:162px;top:946px;font-family:'Oswald',sans-serif;font-weight:400;font-size:30px;color:var(--orange-deep);letter-spacing:1px}
  .ebook{position:absolute;left:353px;top:902px;font-family:'Oswald',sans-serif;font-weight:700;font-size:31px;color:var(--ink)}
  .credit{position:absolute;left:40px;top:1044px;width:719px;text-align:center;font-family:'Oswald',sans-serif;font-weight:700;font-size:21px;line-height:1.5;color:var(--white)}
</style>
</head>
<body>
<div class="canvas">
  <div class="poster">
    <svg class="poster-shapes" width="799" height="1129" viewBox="0 0 799 1129">
      <defs>
        <radialGradient id="soft-glow" cx="0.55" cy="0.45" r="0.6">
          <stop offset="0" stop-color="#f8f7ee"/>
          <stop offset="1" stop-color="#e9e7d8"/>
        </radialGradient>
        <linearGradient id="cover-tone" x1="0" y1="0" x2="0" y2="1">
          <stop offset="0" stop-color="#2e6b4a"/>
          <stop offset="0.45" stop-color="#9fb9a5"/>
          <stop offset="1" stop-color="#f4f5f1"/>
        </linearGradient>
      </defs>
      <rect width="799" height="1129" fill="url(#soft-glow)"/>
      <polygon points="0,0 330,0 0,70" fill="var(--orange)"/>
      <polygon points="735,0 799,0 799,870 770,870 770,270" fill="var(--orange)"/>
      <path d="M0,770 C150,720 280,760 380,780 C560,815 700,800 799,770 L799,1129 L0,1129 Z" fill="var(--orange)"/>
      <path d="M80,790 C160,720 330,740 420,780 C540,830 700,850 799,820 L799,870 C640,900 470,910 300,915 C150,920 60,880 80,790 Z" fill="var(--cream)"/>
      <path d="M80,790 C50,860 140,922 300,916 C470,910 640,900 799,860" fill="none" stroke="var(--green)" stroke-width="4"/>
      <path d="M0,750 C140,690 270,720 360,750" fill="none" stroke="var(--green)" stroke-width="3"/>
    </svg>

    <h1 class="title">VERTENTES</h1>
    <p class="edition">2ª EDIÇÃO</p>

    <svg class="book-stack" viewBox="0 0 455 535" role="img" aria-label="Two copies of the Vertentes 2nd edition book cover, green gradient cover with a blood pressure gauge">
      <polygon points="10,50 345,0 395,455 60,505" fill="#c9cfc7"/>
      <polygon points="10,50 345,0 395,455 60,505" fill="url(#cover-tone)" opacity="0.85"/>
      <polygon points="110,85 430,38 455,490 160,535" fill="#d5d8d2"/>
      <polygon points="105,80 425,32 450,482 155,528" fill="url(#cover-tone)"/>
    </svg>

    <svg class="badge" viewBox="0 0 258 190" aria-hidden="true">
      <ellipse cx="60" cy="110" rx="58" ry="60" fill="#f26a2a"/>
      <ellipse cx="130" cy="55" rx="80" ry="52" fill="#f7c919"/>
      <ellipse cx="200" cy="70" rx="55" ry="60" fill="#79b83b"/>
      <ellipse cx="130" cy="150" rx="95" ry="40" fill="#8fc43f"/>
      <ellipse cx="210" cy="40" rx="35" ry="30" fill="#2aa7dc"/>
      <rect x="45" y="50" width="175" height="95" rx="40" fill="var(--badge-blue)"/>
    </svg>
    <p class="badge-label"><span class="badge-number">1000</span><span class="badge-units">units sold</span></p>

    <p class="publisher">Marlowan</p>
    <p class="ebook">ebook version available...</p>

    <p class="credit">Written by the Vascular Unit of the Southern Clinical Guild of Heart Studies<br>in comemoration in its 100 years.</p>
  </div>
</div>
</body>
</html>
```